Mobile Oil Change company needs a flyer to promote new business

We need a flyer to 1) print & handout and 2) email out to potential customers. We are a mobile oil change company that comes to our customer locations to perform the work instead of customers going to traditional oil change companies. We have a 21 point inspection with our oil change. (21 point inspection details will not be on the flyer). Would like to keep the flyer simple but creative. I'm attaching 1) the write-up we created, 2) our logo (logo color is dark teal on white but other combinations are included if you wanted to propose a different color combination), and 3) additional services we offer. Logo font is Alegreya Sans.
Would like the additional services listed with icons and brief descriptions (similar to attachment) without pricing. Company website for reference is www.brindlefleetcare.com.

Target Market(s)

Companies with many service vehicles such as Oil & Gas service companies, heating and air conditioning companies, utility companies, police departments, etc. Companies that prioritize convenience and maintenance first.

Font styles to use
Sans Serif

Colors
00a990

Requirements
Must have
• Simple but creative design with our logo at top of the flyer. Additional Services (details in document supplied) can be smaller and less prominent than other "main" content listed in the CONTENT document supplied.
Should not have
• Do not use animated character graphics in the flyer and limit (1) stock photos to A small area in the flyer.

```html
<!DOCTYPE html>
<html lang="en">
<head>
<meta charset="utf-8">
<title>Brindle Fleet Care – Mobile Oil Change Flyer</title>
<link href="https://fonts.googleapis.com/css2?family=Alegreya+Sans:wght@300;400;500;700;800&family=Oswald:wght@500;600&family=Alegreya:wght@400;700&display=swap" rel="stylesheet">
<style>
  :root{
    --teal-dark:#17514f;
    --teal:#00a990;
    --ink:#1c3f3e;
    --white:#ffffff;
    --rule:#c9d4d3;
  }
  *{box-sizing:border-box;margin:0;padding:0}
  html,body{width:902px;height:1200px;overflow:hidden;background:#fff}
  .flyer{position:relative;width:902px;height:1200px;overflow:hidden;font-family:"Alegreya Sans",sans-serif;color:var(--ink)}
  .backdrop{position:absolute;inset:0}
  .abs{position:absolute}

  .brand{left:488px;top:40px;width:312px;height:128px;border:3px solid var(--white);border-radius:18px;display:flex;flex-direction:column;align-items:center;justify-content:center;color:var(--white);font-weight:700;text-align:center}
  .brand-name{font-size:50px;line-height:1;letter-spacing:1px}
  .brand-sub{font-size:22px;letter-spacing:5px;margin-top:6px}

  .headline{left:485px;top:236px;width:400px}
  .headline .h1{font-family:"Oswald",sans-serif;font-weight:600;font-size:70px;line-height:1.08;color:var(--teal-dark);letter-spacing:.5px}
  .headline .h2{font-weight:700;font-size:52px;line-height:1.15;color:var(--teal);margin-top:12px}
  .headline .h3{font-weight:700;font-size:41px;line-height:1.2;color:var(--teal-dark);margin-top:4px}

  .intro{left:500px;top:480px;width:390px;color:var(--white);font-size:22px;font-weight:400;line-height:1.45}

  .steps{left:458px;top:574px;width:440px;list-style:none}
  .step{display:flex;align-items:center;height:78px}
  .step-icon{width:64px;height:64px;border-radius:50%;background:var(--white);border:3px solid var(--teal-dark);flex:none;display:flex;align-items:center;justify-content:center}
  .step-text{margin-left:20px;color:var(--white);font-size:18.5px;line-height:1.4;font-weight:500}

  .perks{left:48px;top:598px;width:420px;list-style:none}
  .perks li{position:relative;padding-left:36px;font-size:16.5px;font-weight:700;line-height:1.35;margin-bottom:10px;color:#24302f}
  .perks li::before{content:"";position:absolute;left:0;top:4px;width:14px;height:14px;border-radius:50%;background:var(--teal)}

  .extras-title{left:52px;top:738px;font-size:15px;font-weight:500;letter-spacing:.3px;color:#24302f}
  .services{left:40px;top:796px;width:400px;display:grid;grid-template-columns:repeat(3,1fr);row-gap:14px}
  .service{text-align:center;padding:0 6px;font-family:"Alegreya",serif;font-size:10.5px;line-height:1.3;color:#24302f}
  .service + .service{border-left:1px solid var(--rule)}
  .service:nth-child(4){border-left:none}
  .service svg{display:block;margin:0 auto 8px}
  .service b{display:block;font-size:10.5px;margin-bottom:2px}

  .phone-bar{left:470px;top:1028px;width:432px;height:54px;background:var(--teal);border-radius:27px 0 0 27px;color:var(--white);font-weight:700;font-size:40px;line-height:54px;padding-left:66px}
  .phone-badge{left:456px;top:1018px;width:74px;height:74px}
  .or{left:484px;top:1094px;font-size:12px;font-weight:700;color:var(--teal-dark)}
  .email{left:508px;top:1096px;display:flex;align-items:center;gap:10px;font-size:23px;font-weight:700;color:var(--teal-dark)}

  .web{left:36px;top:1146px;display:flex;align-items:center;gap:12px;color:var(--white);font-size:22px;font-weight:700}
</style>
</head>
<body>
<div class="flyer">

  <svg class="backdrop" width="902" height="1200" viewBox="0 0 902 1200">
    <defs>
      <linearGradient id="photoTone" x1="0" y1="0" x2="1" y2="1">
        <stop offset="0" stop-color="#e9e2d6"/>
        <stop offset=".45" stop-color="#c98a3a"/>
        <stop offset=".7" stop-color="#e8622a"/>
        <stop offset="1" stop-color="#4a4440"/>
      </linearGradient>
    </defs>
    <!-- top band -->
    <path d="M0 0H902V215Q720 175 520 205Q470 212 440 220L0 300Z" fill="var(--teal-dark)"/>
    <path d="M470 196Q680 160 902 212V232Q690 185 470 220Z" fill="var(--teal)"/>
    <!-- wave under visual and step panel -->
    <path d="M150 560Q320 560 440 478Q452 466 470 464H902V1014H520Q460 1014 460 954V520Q360 600 150 585Z" fill="var(--teal-dark)"/>
    <!-- footer tab -->
    <path d="M0 1106H330Q370 1106 395 1150Q418 1200 470 1200H0Z" fill="var(--teal-dark)"/>
    <!-- drop frame -->
    <path d="M210 4C285 110 465 210 465 355C465 465 355 540 230 540C100 540 -10 465 -10 355C-10 210 135 110 210 4Z" fill="var(--white)"/>
  </svg>

  <svg class="abs" style="left:0;top:0" width="470" height="540" viewBox="0 0 470 540" role="img" aria-label="Photo: motor oil being poured from a bottle through an orange funnel into an engine">
    <path d="M210 22C278 120 448 215 448 352C448 452 348 525 228 525C108 525 4 452 4 352C4 215 142 120 210 22Z" fill="url(#photoTone)"/>
  </svg>

  <div class="abs brand">
    <div class="brand-name">BRINDLE</div>
    <div class="brand-sub">FLEET CARE</div>
  </div>

  <div class="abs headline">
    <div class="h1">HASSLE FREE</div>
    <div class="h2">OIL CHANGES</div>
    <div class="h3">ON YOUR TERMS</div>
  </div>

  <p class="abs intro">Our simple 5-step process lets you schedule an appointment and get service to save time and money:</p>

  <ol class="abs steps">
    <li class="step">
      <span class="step-icon"><svg width="34" height="34" viewBox="0 0 34 34" fill="none" stroke="var(--teal-dark)" stroke-width="2"><path d="M6 4l5 0 2 6-3 2c1 3 3 5 6 6l2-3 6 2v5c-11 1-19-7-18-18z"/><rect x="18" y="3" width="13" height="9" rx="1"/><path d="M18 3l6.5 5L31 3"/></svg></span>
      <span class="step-text">Call or email us to schedule service</span>
    </li>
    <li class="step">
      <span class="step-icon"><svg width="34" height="34" viewBox="0 0 34 34" fill="none" stroke="var(--teal-dark)" stroke-width="2"><circle cx="17" cy="9" r="5"/><path d="M8 32V22q0-6 9-6t9 6v10"/><rect x="21" y="24" width="8" height="7"/></svg></span>
      <span class="step-text">Our highly trained technicians come<br>to you for service</span>
    </li>
    <li class="step">
      <span class="step-icon"><svg width="36" height="30" viewBox="0 0 36 30" fill="none" stroke="var(--teal-dark)" stroke-width="2"><path d="M4 18l4-9h18l4 9v7H4z"/><circle cx="10" cy="25" r="3"/><circle cx="26" cy="25" r="3"/><rect x="19" y="14" width="14" height="12" rx="3"/></svg></span>
      <span class="step-text">Service is performed quickly on<br>your vehicle</span>
    </li>
    <li class="step">
      <span class="step-icon"><svg width="34" height="34" viewBox="0 0 34 34" fill="none" stroke="var(--teal-dark)" stroke-width="2"><rect x="4" y="12" width="26" height="18"/><path d="M4 12l13 10 13-10"/><rect x="9" y="4" width="16" height="12"/><text x="17" y="14" font-size="9" text-anchor="middle" fill="var(--teal-dark)" stroke="none">$</text></svg></span>
      <span class="step-text">Pay agreed-upon pricing and receipt<br>is emailed to you</span>
    </li>
    <li class="step">
      <span class="step-icon"><svg width="34" height="34" viewBox="0 0 34 34" fill="none" stroke="var(--teal-dark)" stroke-width="2"><rect x="4" y="16" width="26" height="14"/><path d="M4 16l13 9 13-9"/><path d="M11 14q0-9 6-9t6 9z"/></svg></span>
      <span class="step-text">Services performed are tracked<br>electronically and reminders created</span>
    </li>
  </ol>

  <ul class="abs perks">
    <li>High quality synthetic oil used is best suited for commercial vehicles</li>
    <li>Service includes a 21-point inspection</li>
    <li>Additional services are available</li>
  </ul>

  <div class="abs extras-title">ADDITIONAL SERVICES</div>

  <div class="abs services">
    <div class="service">
      <svg width="34" height="36" viewBox="0 0 34 36" fill="none" stroke="var(--teal)" stroke-width="1.8"><rect x="4" y="3" width="26" height="30"/><path d="M10 3v30M17 3v30M24 3v30"/></svg>
      <b>Engine Air Filter Replacement</b>Maintain optimum engine performance. Recommended every 15,000—30,000 miles.
    </div>
    <div class="service">
      <svg width="34" height="36" viewBox="0 0 34 36" fill="none" stroke="var(--teal)" stroke-width="1.8"><path d="M6 8q5-4 11 0t11 0M6 16q5-4 11 0t11 0M6 24q5-4 11 0t11 0"/><rect x="4" y="3" width="26" height="30" rx="3"/></svg>
      <b>Cabin Air Filter Replacement</b>Maintain a clean A/C and fan system. Recommended every 12 months or 15,000—25,000 miles.
    </div>
    <div class="service">
      <svg width="40" height="36" viewBox="0 0 40 36" fill="none" stroke="var(--teal)" stroke-width="1.8"><path d="M4 24Q20 4 36 24"/><path d="M20 30L28 10"/><path d="M12 12l2 3M20 8v4M28 12l-2 3"/></svg>
      <b>Wiperblade Replacement</b>(Standard) Maintain excellent visibility on the road. Recommended every 6-12 months.
    </div>
    <div class="service">
      <svg width="36" height="36" viewBox="0 0 36 36" fill="none" stroke="var(--teal)" stroke-width="1.8"><circle cx="18" cy="18" r="15"/><circle cx="18" cy="18" r="4"/><path d="M4 16h10M22 16h10M18 22v11"/></svg>
      <b>Power Steering Fluid Flush</b>Maintain proper power steering system health. Recommended every 30,000—60,000 miles.
    </div>
    <div class="service">
      <svg width="34" height="36" viewBox="0 0 34 36" fill="none" stroke="var(--teal)" stroke-width="1.8"><rect x="6" y="4" width="16" height="28" rx="2"/><rect x="9" y="8" width="10" height="7" fill="var(--teal)"/><path d="M22 12h4l2 4v12"/></svg>
      <b>Fuel System Treatment</b>Clean your fuel system and injectors to improve fuel economy.
    </div>
    <div class="service">
      <svg width="38" height="36" viewBox="0 0 38 36" fill="none" stroke="var(--teal)" stroke-width="1.8"><circle cx="18" cy="19" r="14"/><circle cx="18" cy="19" r="5"/><path d="M24 5q10 4 11 14"/></svg>
      <b>Brake Fluid Flush</b>Maintain an excellent functioning brake system. Recommended every 2 years or 20,000 miles.
    </div>
  </div>

  <div class="abs phone-bar">(833) 555-0147</div>
  <svg class="abs phone-badge" width="74" height="74" viewBox="0 0 74 74">
    <circle cx="37" cy="37" r="35" fill="var(--white)"/>
    <path d="M20 16h10l4 12-6 4c3 7 7 11 14 14l4-6 12 4v10C34 56 18 40 20 16z" fill="#111"/>
    <path d="M44 20a12 12 0 0 1 10 10M44 12a20 20 0 0 1 18 18" stroke="#111" stroke-width="3" fill="none"/>
  </svg>
  <div class="abs or">or</div>
  <div class="abs email">
    <svg width="26" height="18" viewBox="0 0 26 18"><rect width="26" height="18" fill="#111"/><path d="M1 1l12 9 12-9" stroke="#fff" stroke-width="2" fill="none"/></svg>
    Sales@BrindleFleetCare.com
  </div>

  <div class="abs web">
    <svg width="20" height="20" viewBox="0 0 20 20" fill="none" stroke="#fff" stroke-width="1.6"><circle cx="10" cy="10" r="8.5"/><ellipse cx="10" cy="10" rx="4" ry="8.5"/><path d="M1.5 10h17M3 5.5h14M3 14.5h14"/></svg>
    www.brindlefleetcare.com
  </div>
</div>
</body>
</html>
```